New Business Card Design

We would like to refresh our business cards and make them look better. We are an IT company specialising in Cloud Services, IT Managed Services, software and hardware. I have attached a PSD of our current design. Also attached our logo.
Updates

I have uploaded all new logos in EPS format.

Can you please edit all designs to include a job title for Marcus Penn, eg. General Manager

Industry/Entity Type

Software

Colors
ffffff

Requirements
Must have
• Please use white background.
Should not have
• Black background

```html
<!DOCTYPE html>
<html lang="en">
<head>
<meta charset="utf-8">
<title>Meridian Systems – Business Card</title>
<link rel="stylesheet" href="https://fonts.googleapis.com/css2?family=Jost:wght@400&family=Source+Sans+3:wght@400&display=swap">
<style>
  :root {
    --page: #ffffff;
    --card: #ffffff;
    --card-edge: #d4d6d9;
    --ink: #1c2530;
    --accent: #c0392b;
    --link: #2f6aa3;
    --rule: #7f93a6;
    --shadow: rgba(0, 0, 0, 0.28);
  }
  html, body {
    margin: 0;
    width: 1200px;
    height: 1000px;
    overflow: hidden;
    background: var(--page);
  }
  .canvas {
    position: relative;
    width: 1200px;
    height: 1000px;
  }
  .card {
    position: absolute;
    width: 738px;
    height: 415px;
    background: var(--card);
    border: 1px solid var(--card-edge);
    box-shadow: 5px 6px 8px var(--shadow);
    box-sizing: border-box;
  }
  .card--front { left: 175px; top: 83px; }
  .card--back  { left: 308px; top: 537px; }

  .brand-dot {
    position: absolute;
    border-radius: 50%;
    background: var(--accent);
  }
  .card--front .brand-dot { left: 72px; top: 50px; width: 58px; height: 58px; }

  .holder-name {
    position: absolute;
    left: 146px;
    top: 44px;
    margin: 0;
    font-family: "Source Sans 3", sans-serif;
    font-weight: 400;
    font-size: 46px;
    line-height: 1;
    color: var(--ink);
  }
  .holder-title {
    position: absolute;
    left: 171px;
    top: 95px;
    margin: 0;
    font-family: "Source Sans 3", sans-serif;
    font-size: 15px;
    letter-spacing: 2.6px;
    color: var(--accent);
  }
  .divider {
    position: absolute;
    left: 37px;
    top: 280px;
    width: 665px;
    height: 1px;
    background: var(--rule);
  }
  .contact {
    position: absolute;
    display: flex;
    align-items: center;
    gap: 9px;
    font-family: "Source Sans 3", sans-serif;
    font-size: 21px;
    color: var(--link);
    line-height: 1;
  }
  .contact svg { width: 28px; height: 28px; flex: none; }
  .contact--office  { left: 38px;  top: 310px; }
  .contact--mobile  { left: 38px;  top: 353px; }
  .contact--email   { left: 406px; top: 310px; }
  .contact--web     { left: 406px; top: 353px; }

  .card--back .brand-dot { left: 188px; top: 142px; width: 74px; height: 74px; }
  .company-name {
    position: absolute;
    left: 285px;
    top: 148px;
    margin: 0;
    font-family: "Jost", sans-serif;
    font-weight: 400;
    color: var(--ink);
    line-height: 1;
  }
  .company-name span { display: block; }
  .company-name .line-1 { font-size: 44px; letter-spacing: 5px; }
  .company-name .line-2 { font-size: 24px; letter-spacing: 4px; margin-top: 8px; padding-left: 40px; }
</style>
</head>
<body>
<main class="canvas">

  <section class="card card--front" aria-label="Business card front">
    <span class="brand-dot" aria-hidden="true"></span>
    <h1 class="holder-name">Marcus Penn</h1>
    <p class="holder-title">GENERAL MANAGER</p>
    <div class="divider"></div>

    <div class="contact contact--office">
      <svg viewBox="0 0 28 28" aria-hidden="true">
        <circle cx="14" cy="14" r="13" fill="var(--accent)"/>
        <path d="M9.5 7.5c.8-.6 1.8-.4 2.3.4l1.2 2c.4.7.2 1.5-.4 2l-.9.7c.8 1.8 2 3 3.7 3.8l.7-.9c.5-.6 1.4-.8 2-.4l2 1.2c.8.5 1 1.5.4 2.3l-.8 1c-.7.9-2 1.2-3 .7-4-1.8-6.8-4.6-8.5-8.6-.4-1 0-2.2.8-2.9z" fill="#fff"/>
      </svg>
      <span>07 3555 0142</span>
    </div>

    <div class="contact contact--mobile">
      <svg viewBox="0 0 28 28" aria-hidden="true">
        <circle cx="14" cy="14" r="13" fill="var(--accent)"/>
        <rect x="9.5" y="6.5" width="9" height="15" rx="1.5" fill="none" stroke="#fff" stroke-width="1.6"/>
        <line x1="9.5" y1="18" x2="18.5" y2="18" stroke="#fff" stroke-width="1.2"/>
      </svg>
      <span>0400 555 217</span>
    </div>

    <div class="contact contact--email">
      <svg viewBox="0 0 28 28" aria-hidden="true">
        <circle cx="14" cy="14" r="13" fill="var(--accent)"/>
        <rect x="7" y="9.5" width="14" height="9.5" rx="1" fill="#fff"/>
        <path d="M7.5 10l6.5 5 6.5-5" fill="none" stroke="var(--accent)" stroke-width="1.3"/>
      </svg>
      <span>mpenn@meridiansys.com.au</span>
    </div>

    <div class="contact contact--web">
      <svg viewBox="0 0 28 28" aria-hidden="true">
        <circle cx="14" cy="14" r="13" fill="var(--accent)"/>
        <g fill="none" stroke="#fff" stroke-width="1.3">
          <circle cx="14" cy="14" r="8"/>
          <ellipse cx="14" cy="14" rx="3.6" ry="8"/>
          <line x1="6" y1="14" x2="22" y2="14"/>
          <path d="M7.5 10h13M7.5 18h13"/>
        </g>
      </svg>
      <span>meridiansys.com.au</span>
    </div>
  </section>

  <section class="card card--back" aria-label="Business card back">
    <span class="brand-dot" aria-hidden="true"></span>
    <h2 class="company-name">
      <span class="line-1">meridian</span>
      <span class="line-2">SYSTEMS</span>
    </h2>
  </section>

</main>
</body>
</html>
```